International Trading Company, 'KIRO' needs a Business Card

The company name is "KIRO" and it has own logo design.
I'd like to use its logo on this business card.
I need two side Business Card.
I'll look forward to your great design.
Thank you very much in advance.

Contact Information for Business Card

Company Name : Kiro Harbour Limited
Information Example
Dorian Pallister
Mobile(use icon please) : 1 (212) 555-0143
Tel(use icon please) : 1 (212) 555-0178
Email(use icon please) : dorian27@kiroharbour-mail.com
Address(use icon please) : 482 Halden Ave, New York, NY 10160, USA

```html
<!DOCTYPE html>
<html lang="en">
<head>
<meta charset="utf-8">
<title>Kiro Harbour Limited – Business Card</title>
<link href="https://fonts.googleapis.com/css2?family=Montserrat:wght@600;700&family=Open+Sans:wght@400;600&display=swap" rel="stylesheet">
<style>
  :root {
    --page: #d9d9d9;
    --card-dark: #0c0c0c;
    --card-light: #ffffff;
    --logo-grey: #5b5b5b;
    --ink: #1a1a1a;
    --muted: #7a7a7a;
    --accent-grey: #6e6e6e;
    --rule: #222222;
  }
  * { margin: 0; padding: 0; box-sizing: border-box; }
  html, body { width: 1200px; height: 864px; overflow: hidden; }
  body {
    background: var(--page);
    position: relative;
    font-family: "Open Sans", Arial, sans-serif;
  }
  .card {
    position: absolute;
    left: 280px;
    width: 640px;
    height: 366px;
    box-shadow: 0 6px 18px rgba(0,0,0,0.25);
    overflow: hidden;
  }
  /* Front side */
  .card-front { top: 46px; background: var(--card-dark); }
  .card-front .wordmark {
    position: absolute;
    top: 92px; left: 0; right: 0;
    text-align: center;
    font-family: "Montserrat", Arial, sans-serif;
    font-weight: 700;
    font-size: 104px;
    letter-spacing: 2px;
    color: var(--logo-grey);
    line-height: 1;
  }
  .card-front .website {
    position: absolute;
    top: 274px; left: 0; right: 0;
    text-align: center;
    color: #ffffff;
    font-size: 19px;
    letter-spacing: 0.5px;
  }
  /* Back side */
  .card-back { top: 452px; background: var(--card-light); }
  .card-back .wordmark {
    position: absolute;
    top: 26px; right: 70px;
    font-family: "Montserrat", Arial, sans-serif;
    font-weight: 700;
    font-size: 76px;
    letter-spacing: 1px;
    color: var(--logo-grey);
    line-height: 1;
  }
  .rule-long {
    position: absolute;
    top: 182px; left: 70px; right: 60px;
    height: 1.5px; background: var(--rule);
  }
  .person { position: absolute; top: 196px; left: 70px; }
  .person .name {
    font-family: "Montserrat", Arial, sans-serif;
    font-weight: 600;
    font-size: 21px;
    color: var(--ink);
  }
  .person .role { font-size: 15px; color: var(--muted); margin-top: 2px; }
  .rule-short {
    position: absolute;
    top: 256px; left: 70px; width: 250px;
    height: 1px; background: var(--rule);
  }
  .contacts {
    position: absolute;
    top: 264px; left: 70px;
    list-style: none;
    font-size: 14px;
    color: #444;
    line-height: 20px;
  }
  .contacts li { display: flex; align-items: center; gap: 8px; }
  .contacts svg { width: 13px; height: 13px; fill: var(--ink); flex: none; }
  .address {
    position: absolute;
    top: 262px; right: 60px;
    text-align: right;
    font-size: 14px;
    line-height: 20px;
    color: #444;
  }
  .edge-band { position: absolute; left: 0; bottom: 0; width: 640px; height: 30px; }
</style>
</head>
<body>

<section class="card card-front" aria-label="Business card front">
  <div class="wordmark">KIRO</div>
  <div class="website">www.kiroharbour-mail.com</div>
</section>

<section class="card card-back" aria-label="Business card back">
  <div class="wordmark">KIRO</div>
  <div class="rule-long"></div>

  <div class="person">
    <div class="name">Dorian Pallister</div>
    <div class="role">President</div>
  </div>
  <div class="rule-short"></div>

  <ul class="contacts">
    <li>
      <svg viewBox="0 0 16 16" aria-hidden="true"><path d="M3.6 1.2l2.2 2.6-1.3 1.8c.9 2 2.4 3.5 4.3 4.3l1.8-1.3 2.6 2.2-1.3 2.4C6.6 13.2 2.8 9.4 1.2 4.1z"/></svg>
      1 (212) 555-0143
    </li>
    <li>
      <svg viewBox="0 0 16 16" aria-hidden="true"><path d="M4.5 0.5h7a1 1 0 0 1 1 1v13a1 1 0 0 1-1 1h-7a1 1 0 0 1-1-1v-13a1 1 0 0 1 1-1zm.6 2v9.5h5.8V2.5zM8 12.8a.9.9 0 1 0 0 1.8.9.9 0 0 0 0-1.8z"/></svg>
      1 (212) 555-0178
    </li>
    <li>
      <svg viewBox="0 0 16 16" aria-hidden="true"><path d="M1 3.5h14v9H1zm1.4 1.2L8 8.9l5.6-4.2z"/></svg>
      dorian27@kiroharbour-mail.com
    </li>
    <li>
      <svg viewBox="0 0 16 16" aria-hidden="true"><path d="M8 1a7 7 0 1 0 0 14A7 7 0 0 0 8 1zm0 1.4c.8 0 1.7 1.5 2 3.8H6c.3-2.3 1.2-3.8 2-3.8zM2.5 7.4h2.3c0 .4 0 .8 0 1.2H2.5zm0 0M6 9.8h4c-.3 2.3-1.2 3.8-2 3.8s-1.7-1.5-2-3.8zm-3.4-3.6A5.6 5.6 0 0 1 5.3 3 9 9 0 0 0 4.6 6.2zm8.8 0A9 9 0 0 0 10.7 3a5.6 5.6 0 0 1 2.7 3.2zM5.8 7.4h4.4v1.2H5.8zm5.4 0h2.3v1.2h-2.3zM2.6 9.8h2a9 9 0 0 0 .7 3.2 5.6 5.6 0 0 1-2.7-3.2zm8.8 0h2a5.6 5.6 0 0 1-2.7 3.2 9 9 0 0 0 .7-3.2z"/></svg>
      www.kiroharbour-mail.com
    </li>
  </ul>

  <div class="address">
    482 Halden Ave,<br>
    New York, NY 10160, USA
  </div>

  <svg class="edge-band" viewBox="0 0 640 30" aria-hidden="true">
    <polygon points="0,18 470,18 462,30 0,30" fill="var(--card-dark)"/>
    <polygon points="484,14 640,0 640,30 474,30" fill="var(--accent-grey)"/>
  </svg>
</section>

</body>
</html>
```